HTML Vorlage für Newsletter von kurortfinder18.de
Zielgruppe
Die Firma marvando GmbH & Co. KG betreibt mit https://www.kurortfinder18.de eine Wellnesshotel Buchungsplattform auf der Erholungssuchende einfach und schnell passende Angebote finden und buchen können.
Für kurortfinder18.de benötigen wir nun eine Design / HTML-Newslettervorlage welche wir zukünftig einsetzen werden.
Aufgabenstellung
Der Aufbau:
Im oberen Bereich sollte sich ein größeres Freifeld befinden, welches wir bei Bedarf mit individuellen Inhalten füllen. Bitte beim Konzept beachten, dass der Bereich nicht immer gefüllt ist und auch leer sein kann (dies wird dann in der Programmierung gesteuert), der Bereich sollte also auch ansprechend aussehen, wenn er nicht gefüllt ist.
Um mittleren Bereich folgen dann untereinander stehend ca. 10 Angebote (mit Arrangementname, Bild, Kurzbeschreibung und Link) aus unserem Portfolio die mir einem optisch schönen "Trenner" zwischen den Angeboten versehen werden sollen.
Im unteren Bereich sollten dann Abmeldelink und Impressum positioniert werden.
Im gesamten soll der Newsletter nicht zu verspielt sein, sondern eher schlicht, aber modern und entsprechend unserer Zielgruppe gestaltet sein.
Auf Anfragen können wir gerne einen Newsletter, der in etwa in die Richtung unserer Vorstellungen geht zusenden.
Bitte CI / CD & Stylguide unbedingt beachten.
Die uneingeschränkten Nutzungsrechte muss nach Abnahme an uns über gehen.
Sollte das Preisgeld zu niedrig angesetzt sein, da wir den Aufwand nicht 100 % einschätzen können, weisen Sie uns bitte darauf hin.
Da wir das Datenformat, welches geliefert werden soll, hier nicht abändern können, hier noch einmal der Hinweis, dass wir die Lieferung als fertiges HTML benötigen. In Ausnahmefällen würde uns die PSD als Gesamtansicht und die einzelnen Grafiken als JPG auch ausreichen. Bevorzugt aber natürlich das fertige HTML.

```html
<!DOCTYPE html>
<html lang="de">
<head>
<meta charset="utf-8">
<title>kurortfinder18 Newsletter</title>
<link rel="stylesheet" href="https://fonts.googleapis.com/css2?family=Arimo:wght@400;700&display=swap">
<style>
  :root {
    --orange: #ee8a1c;
    --orange-dark: #c0651a;
    --peach: #f7c08f;
    --magenta: #d6197e;
    --text: #1a1a1a;
    --muted: #5a5a5a;
    --bg: #ffffff;
  }
  * { margin: 0; padding: 0; box-sizing: border-box; }
  html, body { width: 1067px; height: 1200px; overflow: hidden; background: var(--bg); }
  body { position: relative; font-family: "Arimo", Arial, sans-serif; color: var(--text); }

  .browser-link {
    position: absolute; top: 24px; left: 0; width: 100%;
    text-align: center; font-size: 14px; color: var(--orange); text-decoration: none;
  }
  .brand {
    position: absolute; top: 225px; left: 0; width: 100%;
    display: flex; justify-content: center; align-items: center; gap: 16px;
  }
  .brand-dot {
    width: 22px; height: 22px; border-radius: 50%; background: var(--orange);
  }
  .brand-name {
    font-family: "Arimo", Arial, sans-serif; font-weight: 700;
    font-size: 40px; line-height: 48px; color: var(--muted);
  }
  .header-rule {
    position: absolute; top: 440px; left: 173px; width: 720px; height: 2px;
    background: var(--orange-dark);
  }
  .section-title {
    position: absolute; top: 560px; left: 0; width: 100%; text-align: center;
    font-size: 32px; font-weight: 400; letter-spacing: 1.5px; color: var(--peach);
  }

  .offer-image {
    position: absolute; width: 340px; height: 200px; overflow: hidden;
  }
  .offer-image.spa { background: linear-gradient(135deg, #c9a882 0%, #d9b78f 45%, #b8553a 100%); }
  .offer-image.massage { background: linear-gradient(160deg, #d9e6f2 0%, #e8c9b6 55%, #f2dccd 100%); }
  .offer-image::after {
    content: ""; position: absolute; left: 38%; bottom: -40px; width: 260px; height: 160px;
    border-radius: 50% 50% 0 0; background: rgba(238, 138, 28, .82);
  }
  .offer-image.massage::after { left: -60px; }
  .price {
    position: absolute; z-index: 1; font-size: 30px; font-weight: 700; color: #fff;
  }
  .offer-title {
    position: absolute; font-size: 18px; font-weight: 700; line-height: 24px; color: var(--orange);
  }
  .offer-text {
    position: absolute; font-size: 15.5px; line-height: 24px; color: var(--text);
  }

  .divider-line { position: absolute; top: 951px; height: 2px; background: var(--magenta); }
  .divider-dot {
    position: absolute; top: 922px; left: 518px; width: 30px; height: 30px;
    border-radius: 50%; background: var(--orange); opacity: .8;
  }
</style>
</head>
<body>
  <a class="browser-link" href="https://www.kurortfinder18.de">Browserversion</a>

  <header class="brand">
    <span class="brand-dot"></span>
    <div class="brand-name">kurortfinder18</div>
  </header>
  <div class="header-rule"></div>

  <h1 class="section-title">Ausgewählte Wellness Angebote</h1>

  <article>
    <div class="offer-image spa" style="top:671px; left:173px;" role="img" aria-label="Zwei Frauen in Bademänteln entspannen auf Liegen im Ruheraum">
      <span class="price" style="right:26px; bottom:14px;">ab 195,-</span>
    </div>
    <h2 class="offer-title" style="top:763px; left:553px;">Wellnesswochenende<br>"Individuell"</h2>
    <p class="offer-text" style="top:824px; left:553px;">Wellness Wochenende in der Eifel zum<br>individuell zusammenstellen</p>
  </article>

  <div class="divider-line" style="left:173px; width:234px;"></div>
  <div class="divider-dot"></div>
  <div class="divider-line" style="left:661px; width:231px;"></div>

  <article>
    <div class="offer-image massage" style="top:1003px; left:553px;" role="img" aria-label="Frau bei einer entspannenden Rückenmassage">
      <span class="price" style="left:26px; top:142px;">ab 195,-</span>
    </div>
    <h2 class="offer-title" style="top:1127px; left:173px;">Frühlingserwachen</h2>
    <p class="offer-text" style="top:1160px; left:173px;">Erwecken Sie Körper und Geist mit einer<br>erholsamen Wellnesswoche zu neuem Leben</p>
  </article>
</body>
</html>
```